Velcrest-Aura

Letter heads, business cards, packaging envelopes big and small, and stationery
We have logo design and trademarked approval, we would lie to
upload design to help create this project.
This product was created for my Mother a 4 time diganosed Cancer
Survivor, This product has patent pending and now will be offered to the general public as well.
We are looking foward to working with all of you as this product
and stationary will be viewed worldwide.
Thanks
The Kindale Family

Target Market(s)

all ages and worldwide

Industry/Entity Type

Business

Requirements
Must have
• Our Logo

```html
<!DOCTYPE html>
<html lang="en">
<head>
<meta charset="utf-8">
<title>Velcrest-Aura Stationery</title>
<link href="https://fonts.googleapis.com/css2?family=Signika:wght@700&display=swap" rel="stylesheet">
<style>
  :root {
    --backdrop: #333333;
    --paper: #ffffff;
    --navy: #1c3b6c;
    --red: #b80606;
    --shadow: rgba(0, 0, 0, 0.55);
  }
  * { margin: 0; padding: 0; box-sizing: border-box; }
  html, body { width: 1200px; height: 900px; overflow: hidden; }
  body {
    background: var(--backdrop);
    font-family: "Signika", "Arial Narrow", sans-serif;
    position: relative;
  }
  .sheet {
    position: absolute;
    background: var(--paper);
    box-shadow: 4px 6px 10px var(--shadow);
    overflow: hidden;
  }
  .letterhead { left: 128px; top: 68px; width: 597px; height: 779px; }
  .envelope { left: 468px; top: 215px; width: 630px; height: 241px; border: 1px solid #d6d6d6; }
  .card { left: 791px; width: 252px; height: 145px; border-radius: 10px; }
  .card-front { top: 502px; }
  .card-back { top: 681px; }

  .brand {
    position: absolute;
    display: flex;
    align-items: center;
    color: var(--navy);
  }
  .brand-dot {
    flex: none;
    border-radius: 50%;
    background: var(--red);
  }
  .brand-name {
    font-weight: 700;
    letter-spacing: -0.3px;
    line-height: 1;
    white-space: nowrap;
  }

  .letterhead .brand { left: 32px; top: 30px; gap: 10px; }
  .letterhead .brand-dot { width: 30px; height: 30px; }
  .letterhead .brand-name { font-size: 36px; }

  .envelope .brand { left: 18px; top: 30px; gap: 9px; }
  .envelope .brand-dot { width: 26px; height: 26px; }
  .envelope .brand-name { font-size: 31px; }

  .card .brand { gap: 7px; }
  .card .brand-dot { width: 21px; height: 21px; }
  .card .brand-name { font-size: 26px; }
  .card-front .brand { left: 26px; top: 27px; }
  .card-back .brand { left: 28px; top: 58px; }

  .footer-stripe {
    position: absolute;
    left: 0; right: 0; bottom: 0;
    background: var(--red);
  }
  .footer-stripe::before {
    content: "";
    position: absolute;
    left: 0; right: 0;
    background: var(--navy);
  }
  .letterhead .footer-stripe { height: 20px; }
  .letterhead .footer-stripe::before { top: -7px; height: 3px; }
  .envelope .footer-stripe { height: 19px; }
  .envelope .footer-stripe::before { top: -5px; height: 3px; }
  .card .footer-stripe { height: 22px; }
  .card .footer-stripe::before { top: -5px; height: 3px; }
</style>
</head>
<body>
  <section class="sheet letterhead">
    <div class="brand">
      <span class="brand-dot"></span>
      <span class="brand-name">Velcrest-Aura</span>
    </div>
    <div class="footer-stripe"></div>
  </section>

  <section class="sheet envelope">
    <div class="brand">
      <span class="brand-dot"></span>
      <span class="brand-name">Velcrest-Aura</span>
    </div>
    <div class="footer-stripe"></div>
  </section>

  <section class="sheet card card-front">
    <div class="brand">
      <span class="brand-dot"></span>
      <span class="brand-name">Velcrest-Aura</span>
    </div>
    <div class="footer-stripe"></div>
  </section>

  <section class="sheet card card-back">
    <div class="brand">
      <span class="brand-dot"></span>
      <span class="brand-name">Velcrest-Aura</span>
    </div>
  </section>
</body>
</html>
```